Book cover for "Skinward Turning"

Hi, we need a book cover for "Skinward Turning" book.
It's a book about how to cure psoriasis symptoms which appeared to be results of stress.
The main theme in this book is that all symptoms are psychosomatic and can be cut short by reducing the level of stress.
Cover has to be bold and speaking. It has to show the results,
PLEASE consider using photos or illustrations "before" and "after".
Or maybe you can propose your vision.

3D image and 2D image.
Please see the links, it will be helpful for you to create image form.
http://kw7rnpfa.lintrova.com/?skip-tracking=true
http://zt3mxbvc.lintrova.com/?skip-tracking=true

Target Market(s)

TA is very wide, it's all people who experienced decease demonstration. Usually these people very embarrassed of their illness, they are under high level of stress and what they need it's hope and believe that they can relief their condition.

Requirements
Must have
• Author name:
Oleg Varnik
Titlle :
Skinward Turning
Subtitle:
SKINWARD TURNING:
REDUCE THE RASH AND ITCHING 73% WITH THIS SIMPLE TECHNIQUE

```html
<!DOCTYPE html>
<html lang="en">
<head>
<meta charset="utf-8">
<title>Skinward Turning — Book Cover</title>
<link rel="stylesheet" href="https://fonts.googleapis.com/css2?family=Antonio:wght@300;400&family=Open+Sans:wght@600&family=Tinos:wght@400;700&family=IM+Fell+English:ital@1&display=swap">
<style>
  :root {
    --sky-top: #06d4ef;
    --sky-mid: #14bfe0;
    --sky-low: #1aa3c6;
    --white: #ffffff;
    --band: #0f86be;
    --band-light: #1796c8;
    --frame: #d8dde0;
    --photo-skin: #b86a5e;
    --photo-hand: #c9836f;
    --photo-herb: #a8926a;
  }
  * { margin: 0; padding: 0; box-sizing: border-box; }
  html, body { width: 1200px; height: 900px; overflow: hidden; }
  body { background: var(--sky-low); }
  .cover {
    position: relative; width: 1200px; height: 900px; overflow: hidden;
    background: linear-gradient(180deg, var(--sky-top) 0%, var(--sky-mid) 55%, var(--sky-low) 100%);
    color: var(--white);
  }
  .rule { position: absolute; left: 0; width: 1200px; height: 3px; background: var(--white); }
  .rule--top-a { top: 103px; } .rule--top-b { top: 113px; }
  .rule--bottom-a { top: 778px; } .rule--bottom-b { top: 788px; }

  .side-bands { position: absolute; left: 0; top: 0; }

  .back-glow {
    position: absolute; left: 160px; top: 380px; width: 360px; height: 360px;
    background: radial-gradient(circle at 40% 50%, rgba(200,240,200,0.55) 0%, rgba(150,220,220,0.25) 45%, rgba(20,190,224,0) 72%);
  }
  .front-hand {
    position: absolute; left: 640px; top: 260px; width: 300px; height: 400px;
    background: radial-gradient(ellipse at 55% 55%, rgba(120,200,225,0.45) 0%, rgba(20,190,224,0) 70%);
  }

  .title {
    position: absolute; right: 66px; top: 10px;
    font-family: "Antonio", sans-serif; font-weight: 300;
    font-size: 56px; line-height: 56px; letter-spacing: 2px; white-space: nowrap;
  }
  .subtitle {
    position: absolute; right: 48px; top: 69px;
    font-family: "Open Sans", sans-serif; font-weight: 600;
    font-size: 12.5px; line-height: 16px; letter-spacing: 0.9px; white-space: nowrap;
  }

  .about { position: absolute; left: 48px; top: 424px; width: 464px; }
  .about__heading {
    font-family: "Tinos", serif; font-weight: 400;
    font-size: 27px; letter-spacing: 2.5px; margin-bottom: 18px;
  }
  .about__text {
    font-family: "Tinos", serif; font-weight: 700;
    font-size: 14.6px; line-height: 32.5px; text-align: justify; hyphens: auto;
  }
  .about__signature {
    text-align: right; margin-top: 4px;
    font-family: "IM Fell English", serif; font-style: italic; font-size: 22px;
  }

  .spine {
    position: absolute; left: 595px; top: 497px;
    transform: translate(-50%, -50%) rotate(-90deg);
    white-space: nowrap; display: flex; align-items: baseline; gap: 30px;
    font-family: "Antonio", sans-serif; font-weight: 300;
  }
  .spine__title { font-size: 44px; letter-spacing: 1.5px; }
  .spine__author { font-size: 24px; letter-spacing: 1px; position: relative; top: -8px; }

  .photo {
    position: absolute; border: 3px solid var(--frame);
    box-shadow: 0 2px 6px rgba(0,0,0,0.25);
  }
  .photo--elbows { left: 742px; top: 206px; width: 174px; height: 144px; z-index: 2;
    background: linear-gradient(160deg, #3a3f4a 0%, var(--photo-skin) 50%, #2a3c7a 100%); }
  .photo--cream { left: 815px; top: 287px; width: 328px; height: 270px; z-index: 1;
    background: linear-gradient(135deg, #f3f3f3 0%, var(--photo-hand) 40%, #a8493e 100%); }
  .photo--herbs { left: 995px; top: 468px; width: 195px; height: 162px; z-index: 3;
    background: linear-gradient(135deg, #f4f0ea 0%, var(--photo-herb) 50%, #6b5a7e 100%); }

  .author {
    position: absolute; left: 830px; top: 806px;
    font-family: "Antonio", sans-serif; font-weight: 300;
    font-size: 54px; letter-spacing: 2px; white-space: nowrap;
  }
</style>
</head>
<body>
<main class="cover">
  <div class="back-glow" role="img" aria-label="Faint photo of hands holding a soothing object"></div>
  <div class="front-hand" role="img" aria-label="Faint photo of a hand in the background"></div>

  <svg class="side-bands" width="1200" height="900" aria-hidden="true">
    <rect x="930" y="225" width="270" height="10" fill="var(--band-light)" opacity="0.8"/>
    <rect x="930" y="245" width="270" height="10" fill="var(--band)" opacity="0.8"/>
    <rect x="950" y="655" width="250" height="10" fill="var(--band-light)" opacity="0.8"/>
    <rect x="950" y="675" width="250" height="10" fill="var(--band)" opacity="0.8"/>
  </svg>

  <div class="rule rule--top-a"></div>
  <div class="rule rule--top-b"></div>
  <div class="rule rule--bottom-a"></div>
  <div class="rule rule--bottom-b"></div>

  <h1 class="title">Skinward Turning</h1>
  <p class="subtitle">Reduce The Rash And Itching 73% With This Simple Technique</p>

  <section class="about">
    <h2 class="about__heading">About this book</h2>
    <p class="about__text">Lorem ipsum dolor sit amet, consectetur adipisicing elit, sed do eiusmod, quis nostrud exercitation ullamco laboris nisi ut aliquip ex ea commodo consequat. Duis aute irure dolor in reprehenderit in voluptate velit esse cillum dolore eu fugiat nulla pariatur. Excepteur sint occaecat cupidatat non proident, sunt in culpa qui officia deserunt mollit anim id est laborum."</p>
    <p class="about__signature">Oleg Varnik</p>
  </section>

  <div class="spine">
    <span class="spine__title">Skinward Turning</span>
    <span class="spine__author">Oleg Varnik</span>
  </div>

  <div class="photo photo--elbows" role="img" aria-label="Photo of elbows with psoriasis patches"></div>
  <div class="photo photo--cream" role="img" aria-label="Photo of a hand squeezing cream from a tube onto a fingertip"></div>
  <div class="photo photo--herbs" role="img" aria-label="Photo of herbs, mortar and pestle and oil bottles"></div>

  <p class="author">Oleg Varnik</p>
</main>
</body>
</html>
```